Construction Company business card and Logo.

We need a business card for a Building Company.
We build and constuction manage.
A simple logo is also required. Ive attached some samples that may assist.
Logo colours: Blue,sunburnt orange,lime/green and brown/grey.
The Font for the Brevanta logo ive been using is Georgia.
Maybe the A in Brevanta can be like my logo design..?
All other font either calibri or arial, something simple.
Simple/modern and neat is what i am looking for.
My card should look organised to convey what the company is about.

Target Market(s)

Developers, architects, proffesionals in general

Industry/Entity Type

Business

Contact Information for Business Card

Brevanta Constructions Pty Ltd
ACN: 381 607 925 Lic:716382D
Dermot Halvorsen
Managing Director
0438 215 706
dermot@brevanta.com.au
www.brevanta.com.au
Industrial.Commercial.Residential.Build Management

Requirements
Must have
• Ive attached some ideas for the logo. Its simple. If you come up with something else, please show me as im not 100% sure of what i want.
The front of the card should be white.
The back of the card should have the company name and logo with Blue background
Should not have
• the design should be simple.
No old style fonts or italics etc

```html
<!DOCTYPE html>
<html lang="en">
<head>
<meta charset="utf-8">
<title>Brevanta Constructions Pty Ltd – Business Card</title>
<link rel="stylesheet" href="https://fonts.googleapis.com/css2?family=Open+Sans:wght@400;600;700&display=swap">
<style>
  :root {
    --stage: #3a3a3c;
    --card-blue: #1d5c7b;
    --card-white: #ffffff;
    --brand-brown: #a35d3f;
    --ink-blue: #1c5f86;
    --ink-grey: #555a5e;
    --tag-blue: #9cc3d8;
    --accent-teal: #2a6f98;
  }
  * { box-sizing: border-box; margin: 0; padding: 0; }
  html, body {
    width: 1200px; height: 900px; overflow: hidden;
    background: var(--stage);
    font-family: "Open Sans", Arial, sans-serif;
  }
  .canvas {
    width: 1200px; height: 900px;
    display: flex; flex-direction: column; align-items: center; justify-content: center;
    gap: 40px;
  }
  .card {
    width: 620px; height: 378px;
    position: relative;
    box-shadow: 0 10px 30px rgba(0,0,0,.35);
  }
  .card--back { background: var(--card-blue); }
  .card--front { background: var(--card-white); }

  .wordmark { display: flex; align-items: center; gap: 14px; }
  .wordmark__text { color: var(--brand-brown); font-weight: 700; line-height: 1; }
  .wordmark__name { display: block; font-size: 46px; letter-spacing: 1px; }
  .wordmark__sub { display: block; font-size: 13px; letter-spacing: 1.5px; margin-top: 4px; text-align: right; }
  .wordmark__square { width: 44px; height: 44px; background: var(--accent-teal); }

  .card--back .wordmark {
    position: absolute; left: 50%; top: 128px; transform: translateX(-50%);
  }
  .services {
    position: absolute; left: 0; right: 0; bottom: 62px;
    text-align: center; color: var(--tag-blue); font-size: 14px; letter-spacing: .3px;
  }

  .card--front .wordmark { position: absolute; left: 150px; top: 46px; }
  .card--front .wordmark__name { font-size: 40px; }
  .card--front .wordmark__sub { font-size: 11px; }
  .card--front .wordmark__square { width: 38px; height: 38px; }

  .person { position: absolute; left: 46px; top: 150px; color: var(--ink-blue); }
  .person__name { font-size: 19px; font-weight: 400; letter-spacing: 1px; text-transform: uppercase; }
  .person__role { font-size: 15px; margin-top: 2px; }

  .contact { position: absolute; left: 46px; top: 218px; list-style: none; font-size: 12.5px; color: var(--ink-blue); line-height: 1.55; }
  .contact__label { font-weight: 700; display: inline-block; width: 14px; }

  .registration {
    position: absolute; right: 40px; bottom: 30px;
    font-size: 11.5px; color: var(--ink-grey); line-height: 1.4;
  }
</style>
</head>
<body>
<main class="canvas">
  <section class="card card--back" aria-label="Card back">
    <div class="wordmark">
      <div class="wordmark__text">
        <span class="wordmark__name">Brevanta</span>
        <span class="wordmark__sub">Constructions Pty Ltd</span>
      </div>
      <span class="wordmark__square" aria-hidden="true"></span>
    </div>
    <p class="services">Industrial • Commercial • Residential • Build Management</p>
  </section>

  <section class="card card--front" aria-label="Card front">
    <div class="wordmark">
      <div class="wordmark__text">
        <span class="wordmark__name">Brevanta</span>
        <span class="wordmark__sub">Constructions Pty Ltd</span>
      </div>
      <span class="wordmark__square" aria-hidden="true"></span>
    </div>
    <div class="person">
      <h1 class="person__name">Dermot Halvorsen</h1>
      <p class="person__role">Managing Director</p>
    </div>
    <ul class="contact">
      <li><span class="contact__label">p</span> 0438 215 706</li>
      <li><span class="contact__label">e</span> dermot@brevanta.com.au</li>
      <li><span class="contact__label">w</span> www.brevanta.com.au</li>
    </ul>
    <p class="registration">ACN: 381 607 925<br>Lic:716382D</p>
  </section>
</main>
</body>
</html>
```